Fresh & clean business card for yacht detailing company
Gullrock detailing
Professional
Captain Morgan tellaver
President
PO box 827 Speonk, ny 11846
Morgan@Gullrockdetailing.com
Gullrockdetailing.com
mtellaver mtellaver
pixelharborworks: #271 - i really like this design, can you add a touch of silver/gray to it?
quillmotionlab: #140 - i really like the back with the logo splitting the blue on bottom & black on top. #142 - i really like the front with the logo in the color at the bottom. can you take the back of #140, put it with the front of #142. Id like to see the color at the bottom in blue and another draft in black?
#34 - maybe a slightly larger logo on front of card?

```html
<!DOCTYPE html>
<html lang="en">
<head>
<meta charset="utf-8">
<title>Gullrock detailing — business card</title>
<link rel="stylesheet" href="https://fonts.googleapis.com/css2?family=Cinzel:wght@700&family=Montserrat:wght@400;500;600&display=swap">
<style>
  :root {
    --navy: #1f3f7a;
    --ink: #2b2b33;
    --grey: #8a8f99;
    --paper: #ffffff;
    --backdrop: #eceef1;
  }
  html, body {
    margin: 0;
    padding: 0;
    width: 1200px;
    height: 906px;
    overflow: hidden;
    background: var(--backdrop);
  }
  .canvas {
    width: 1200px;
    height: 906px;
    display: flex;
    align-items: center;
    justify-content: center;
    gap: 60px;
  }
  .card {
    width: 525px;
    height: 300px;
    background: var(--paper);
    box-shadow: 0 6px 20px rgba(0,0,0,0.12);
    position: relative;
    box-sizing: border-box;
    overflow: hidden;
  }
  .wordmark {
    font-family: "Cinzel", serif;
    font-weight: 700;
    color: var(--navy);
    text-transform: uppercase;
    letter-spacing: 1px;
    margin: 0;
    line-height: 1;
    white-space: nowrap;
  }
  .tagline {
    font-family: "Montserrat", sans-serif;
    font-weight: 500;
    color: var(--navy);
    margin: 6px 0 0;
    letter-spacing: 0.3px;
    white-space: nowrap;
  }
  /* front */
  .front .brand {
    position: absolute;
    top: 44px;
    left: 212px;
    width: 290px;
    text-align: center;
  }
  .front .wordmark { font-size: 21px; }
  .front .tagline { font-size: 9px; }
  .person {
    position: absolute;
    top: 120px;
    left: 212px;
    width: 290px;
    text-align: center;
    font-family: "Montserrat", sans-serif;
  }
  .person-name {
    margin: 0;
    font-size: 13px;
    font-weight: 600;
    letter-spacing: 1px;
    color: var(--ink);
    text-transform: uppercase;
  }
  .person-role {
    margin: 4px 0 0;
    font-size: 9px;
    letter-spacing: 1.5px;
    color: var(--grey);
    text-transform: uppercase;
  }
  .contact-list {
    position: absolute;
    list-style: none;
    margin: 0;
    padding: 0;
    font-family: "Montserrat", sans-serif;
    font-size: 8.5px;
    color: var(--ink);
  }
  .contact-list li {
    display: flex;
    align-items: center;
    gap: 7px;
    height: 18px;
    white-space: nowrap;
  }
  .contact-list svg { flex: none; }
  .contact-main { top: 40px; left: 20px; }
  .contact-web { bottom: 22px; right: 24px; }
  /* back */
  .back {
    display: flex;
    flex-direction: column;
    align-items: center;
    justify-content: center;
    text-align: center;
  }
  .back .wordmark { font-size: 34px; }
  .back .tagline { font-size: 13px; margin-top: 10px; }
</style>
</head>
<body>
<main class="canvas">
  <section class="card front" aria-label="Card front">
    <ul class="contact-list contact-main">
      <li>
        <svg width="12" height="12" viewBox="0 0 12 12"><rect width="12" height="12" fill="var(--navy)"/><path d="M6 2.5a2.2 2.2 0 0 0-2.2 2.2C3.8 6.4 6 9.5 6 9.5s2.2-3.1 2.2-4.8A2.2 2.2 0 0 0 6 2.5z" fill="#fff"/></svg>
        PO box 827 Speonk, NY 11846
      </li>
      <li>
        <svg width="12" height="12" viewBox="0 0 12 12"><rect width="12" height="12" fill="var(--navy)"/><path d="M3.5 2.5l1.5 0 .6 1.8-.9.7a5 5 0 0 0 2.3 2.3l.7-.9 1.8.6v1.5c-3.5.3-6.3-2.5-6-6z" fill="#fff"/></svg>
        631 - 555 - 0192
      </li>
      <li>
        <svg width="12" height="12" viewBox="0 0 12 12"><rect width="12" height="12" fill="var(--navy)"/><rect x="2.5" y="3.5" width="7" height="5" fill="none" stroke="#fff" stroke-width="0.9"/><path d="M2.5 3.5L6 6.3 9.5 3.5" fill="none" stroke="#fff" stroke-width="0.9"/></svg>
        Morgan@Gullrockdetailing.com
      </li>
    </ul>

    <div class="brand">
      <p class="wordmark">Gullrock detailing</p>
      <p class="tagline">Professional Polishing &amp; Yacht Maintenance</p>
    </div>

    <div class="person">
      <p class="person-name">Morgan Tellaver</p>
      <p class="person-role">President</p>
    </div>

    <ul class="contact-list contact-web">
      <li>
        <svg width="12" height="12" viewBox="0 0 12 12"><rect width="12" height="12" fill="var(--navy)"/><circle cx="6" cy="6" r="3.2" fill="none" stroke="#fff" stroke-width="0.9"/><path d="M2.8 6h6.4M6 2.8v6.4" stroke="#fff" stroke-width="0.7"/></svg>
        Gullrockdetailing.com
      </li>
      <li>
        <svg width="12" height="12" viewBox="0 0 12 12"><rect width="12" height="12" fill="var(--navy)"/></svg>
        mtellaver
      </li>
      <li>
        <svg width="12" height="12" viewBox="0 0 12 12"><rect width="12" height="12" fill="var(--navy)"/></svg>
        mtellaver
      </li>
    </ul>
  </section>

  <section class="card back" aria-label="Card back">
    <p class="wordmark">Gullrock detailing</p>
    <p class="tagline">Professional Polishing &amp; Yacht Maintenance</p>
  </section>
</main>
</body>
</html>
```